Stationary & Business Card for Talvo Co, LLC
Talvo Co, LLC
Professional
Adrian Pellworth, MD
President
2918 Larkfield Ave., Suite C-240
Bethesda, MD 20846
dradrian@talvocollc.com
www.talvocollc.com
Our tagline is Your Partner in Personalized Healthcare.
We would like a solid color for our back - either matching the purple or gold of our logo

```html
<!DOCTYPE html>
<html lang="en">
<head>
<meta charset="utf-8">
<title>Talvo Co, LLC — Business Card</title>
<link href="https://fonts.googleapis.com/css2?family=Open+Sans:ital,wght@0,400;0,600;1,400&display=swap" rel="stylesheet">
<style>
  :root {
    --purple: #5a2a6c;
    --purple-line: #6e3a82;
    --white: #ffffff;
    --ink: #3a3a3a;
    --stage: #e6e6e8;
    --soft: #e9dcef;
  }
  * { margin: 0; padding: 0; box-sizing: border-box; }
  html, body { width: 1200px; height: 838px; overflow: hidden; }
  body {
    background: var(--stage);
    font-family: "Open Sans", Arial, sans-serif;
    display: flex;
    flex-direction: column;
    align-items: center;
    justify-content: center;
    gap: 40px;
  }
  .card {
    width: 640px;
    height: 366px;
    background: var(--white);
    box-shadow: 0 6px 18px rgba(0,0,0,.18);
    position: relative;
    overflow: hidden;
  }
  /* Front */
  .card-front { display: flex; }
  .contact-panel {
    width: 54%;
    background: var(--purple);
    color: var(--white);
    padding: 34px 30px;
  }
  .holder-name { font-size: 22px; font-weight: 600; letter-spacing: .2px; }
  .holder-title { font-size: 14px; font-style: italic; margin-top: 2px; opacity: .9; }
  .contact-list { list-style: none; margin-top: 70px; }
  .contact-list li {
    display: flex; align-items: center; gap: 10px;
    font-size: 12px; line-height: 1; margin-bottom: 9px;
  }
  .contact-list .plain { padding-left: 24px; margin-top: -4px; }
  .icon {
    width: 14px; height: 14px; border-radius: 50%;
    background: var(--white); flex: none;
    display: flex; align-items: center; justify-content: center;
  }
  .icon svg { width: 9px; height: 9px; fill: var(--purple); }
  .brand-panel {
    flex: 1;
    display: flex; align-items: center; justify-content: center;
    padding: 26px;
  }
  .brand-frame {
    width: 100%; height: 100%;
    border: 4px solid var(--purple-line);
    display: flex; align-items: center; justify-content: center;
  }
  .brand-mark { display: flex; align-items: center; gap: 10px; }
  .brand-dot { width: 34px; height: 34px; border-radius: 50%; background: var(--purple); }
  .brand-name { font-size: 24px; font-weight: 600; color: var(--purple); }
  /* Back */
  .card-back {
    display: flex; flex-direction: column;
    align-items: center; justify-content: center; gap: 36px;
  }
  .card-back .brand-dot { width: 64px; height: 64px; }
  .card-back .brand-name { font-size: 30px; }
  .back-web { font-size: 14px; letter-spacing: 3px; color: var(--ink); }
</style>
</head>
<body>
  <section class="card card-front" aria-label="Business card front">
    <div class="contact-panel">
      <h1 class="holder-name">Adrian Pellworth, MD</h1>
      <p class="holder-title">President</p>
      <ul class="contact-list">
        <li><span class="icon"><svg viewBox="0 0 10 10"><path d="M5 0a3.5 3.5 0 0 0-3.5 3.5C1.5 6 5 10 5 10s3.5-4 3.5-6.5A3.5 3.5 0 0 0 5 0zm0 5a1.5 1.5 0 1 1 0-3 1.5 1.5 0 0 1 0 3z"/></svg></span>2918 Larkfield Ave., Suite C-240</li>
        <li class="plain">Bethesda, MD 20846</li>
        <li><span class="icon"><svg viewBox="0 0 10 10"><path d="M2 0l2 2.5-1 1.2a6 6 0 0 0 3.3 3.3l1.2-1L10 8l-1.5 2C4 10 0 6 0 1.5z"/></svg></span>(301) 555-0142</li>
        <li><span class="icon"><svg viewBox="0 0 10 10"><rect x="1" y="3" width="8" height="5"/><rect x="3" y="0.5" width="4" height="2"/></svg></span>(301) 555-0187</li>
        <li><span class="icon"><svg viewBox="0 0 10 10"><path d="M0 2h10v6H0zM0 2l5 3.5L10 2" stroke="#5a2a6c" stroke-width=".6"/></svg></span>dradrian@talvocollc.com</li>
        <li><span class="icon"><svg viewBox="0 0 10 10"><circle cx="5" cy="5" r="4.5"/></svg></span>www.talvocollc.com</li>
      </ul>
    </div>
    <div class="brand-panel">
      <div class="brand-frame">
        <div class="brand-mark">
          <span class="brand-dot"></span>
          <span class="brand-name">Talvo Co, LLC</span>
        </div>
      </div>
    </div>
  </section>

  <section class="card card-back" aria-label="Business card back">
    <div class="brand-mark">
      <span class="brand-dot"></span>
      <span class="brand-name">Talvo Co</span>
    </div>
    <p class="back-web">www.talvocollc.com</p>
  </section>
</body>
</html>
```